Corvane Stationery Design

We need design for our stationary, including:
1) Letterhead
- A4/Letter size in landscape and portrait letterhead
- The letterhead must be in a word file, and the address should be editable using the Felixti or Perpetua Titling TTF
- The output file should be in .docx and in .ai.
2) Business card
- The business card will be printed in white paper and single face only, so there should be nothing on the reverse side.
3) Envelope (sizes A4, Letter, and small document)
Please refer to the picture showing some samples of stationary with designs that would fulfill our wish.
We're including the logo in .AI.
Thanks
Target Market(s)
High end investors
Industry/Entity Type
Landscape
Look and feel

```html
<!DOCTYPE html>
<html lang="en">
<head>
<meta charset="utf-8">
<title>Corvane Business Cards</title>
<link href="https://fonts.googleapis.com/css2?family=Mulish:wght@400;600;700&display=swap" rel="stylesheet">
<style>
  :root {
    --stage: #4a4a4a;
    --card: #f7f7f6;
    --ink: #444444;
    --ink-soft: #6a6a6a;
    --brand-blue: #1a5a8a;
    --bar-dark: #3b3b3b;
  }
  html, body {
    margin: 0;
    padding: 0;
    width: 1200px;
    height: 1000px;
    overflow: hidden;
    background: var(--stage);
    font-family: "Mulish", sans-serif;
  }
  .stage {
    position: relative;
    width: 1200px;
    height: 1000px;
  }
  .card {
    position: absolute;
    width: 532px;
    height: 303px;
    background: var(--card);
    color: var(--ink);
    box-shadow: 0 3px 8px rgba(0,0,0,0.35);
  }
  .card--primary { left: 205px; top: 163px; }
  .card--alternate { left: 470px; top: 533px; }

  .brand-name {
    position: absolute;
    left: 40px;
    top: 50px;
    margin: 0;
    font-size: 36px;
    font-weight: 600;
    letter-spacing: 4px;
    color: var(--brand-blue);
    line-height: 1;
  }
  .person-name {
    position: absolute;
    margin: 0;
    font-size: 15px;
    font-weight: 700;
    color: var(--ink);
    letter-spacing: 0.3px;
  }
  .person-title {
    position: absolute;
    margin: 0;
    font-size: 10px;
    color: var(--ink-soft);
  }
  .address {
    position: absolute;
    margin: 0;
    font-size: 11px;
    line-height: 16px;
    font-style: normal;
    color: var(--ink);
  }
  .contact-list {
    position: absolute;
    margin: 0;
    padding: 0;
    list-style: none;
    font-size: 11px;
    color: var(--ink);
  }
  .card--primary .contact-list li { height: 18px; }
  .card--primary .contact-label { color: var(--brand-blue); }
  .card--alternate .contact-list li { height: 25px; }
  .card--alternate .contact-label { font-weight: 700; color: var(--ink); }

  .card-bars {
    position: absolute;
    left: 0;
    bottom: 0;
    width: 100%;
    height: 10px;
  }
  .card-bars .bar-dark {
    position: absolute; left: 0; top: 0; width: 192px; height: 10px;
    background: var(--bar-dark);
  }
  .card-bars .bar-blue {
    position: absolute; left: 196px; top: 0; right: 0; height: 10px;
    background: var(--brand-blue);
  }
</style>
</head>
<body>
<main class="stage">

  <section class="card card--primary">
    <h1 class="brand-name">CORVANE</h1>
    <h2 class="person-name" style="left:353px; top:136px;">ADRIAN HOLLOWAY</h2>
    <p class="person-title" style="left:353px; top:159px;">Chairman</p>
    <ul class="contact-list" style="left:353px; top:199px;">
      <li><span class="contact-label">Mobile:</span> +877 555 2140</li>
      <li><span class="contact-label">Phone:</span> +877 555 2140</li>
      <li><span class="contact-label">Email:</span> info@corvane.com</li>
      <li><span class="contact-label">Web:</span> www.corvane.com</li>
    </ul>
    <address class="address" style="left:40px; top:236px;">
      218 Harlow Street 3rd Floor<br>Brookfield, CA 94108
    </address>
    <div class="card-bars"><span class="bar-dark"></span><span class="bar-blue"></span></div>
  </section>

  <section class="card card--alternate">
    <h1 class="brand-name">CORVANE</h1>
    <h2 class="person-name" style="left:40px; top:175px;">ADRIAN HOLLOWAY</h2>
    <p class="person-title" style="left:40px; top:198px;">Chairman</p>
    <address class="address" style="left:40px; top:236px;">
      218 Harlow Street 3rd Floor<br>Brookfield, CA 94108
    </address>
    <ul class="contact-list" style="left:354px; top:176px;">
      <li><span class="contact-label">Mobile:</span> +877 555 2140</li>
      <li><span class="contact-label">Email:</span> info@corvane.com</li>
      <li><span class="contact-label">Phone:</span> +877 555 2140</li>
      <li><span class="contact-label">Web:</span> www.corvane.com</li>
    </ul>
    <div class="card-bars"><span class="bar-dark"></span><span class="bar-blue"></span></div>
  </section>

</main>
</body>
</html>
```